Aussie Electrician needs Business Card,

Velkor Electrical Services requires a,business card design.. Company colours are black, flouo orange and silver. Refer to attached photos of company shirt.. I was thinking of basing the business card around the company shirt as company vehicle will be black with similar graphics. The business card will need to include my mobile phone number which is 0400 518 067, my business address which is P.O. Box 863, Narrabeen, N.S.W., 2101, my email which is greg@velkorelectrical.com.au as well as my contractor licence number which is 5143K

Industry/Entity Type

Business

Contact Information for Business Card

mobile: 0400 518 067, email: greg@velkorelectrical.com.au,address :P.O. Box 863 TALLOWOOD NSW 2164, Contractor Lic No 5143K, Greg Halloway

Requirements
Must have
• Refer to photos of shirt. Gloss black background

```html
<!DOCTYPE html>
<html lang="en">
<head>
<meta charset="utf-8">
<title>Greg Halloway — Business Card</title>
<link rel="stylesheet" href="https://fonts.googleapis.com/css2?family=Source+Sans+3:wght@400;500;600&display=swap">
<style>
  :root {
    --page: #ffffff;
    --card-black: #000000;
    --card-charcoal: #3b3939;
    --card-brown: #1e1815;
    --flouro-orange: #e0694a;
    --silver: #8a8888;
    --text-white: #ffffff;
  }
  * { margin: 0; padding: 0; box-sizing: border-box; }
  html, body {
    width: 1200px;
    height: 900px;
    overflow: hidden;
    background: var(--page);
  }
  .business-card {
    position: absolute;
    left: 116px;
    top: 172px;
    width: 944px;
    height: 565px;
    overflow: hidden;
    background:
      radial-gradient(ellipse 480px 420px at 880px 210px, var(--card-charcoal) 0%, var(--card-brown) 55%, rgba(0,0,0,0) 100%),
      linear-gradient(90deg, var(--card-black) 0%, #0d0806 50%, var(--card-brown) 100%);
    font-family: "Source Sans 3", "Myriad Pro", sans-serif;
    color: var(--text-white);
  }
  .holder-name {
    position: absolute;
    left: 87px;
    top: 86px;
    font-size: 41px;
    font-weight: 400;
    letter-spacing: 0;
    line-height: 1;
  }
  .licence-number {
    position: absolute;
    left: 89px;
    top: 147px;
    font-size: 16px;
    font-weight: 500;
  }
  .contact-tab {
    position: absolute;
    left: 0;
    top: 248px;
    width: 64px;
    height: 212px;
    background: var(--flouro-orange);
    border-radius: 0 16px 16px 0;
  }
  .contact-list {
    position: absolute;
    left: 0;
    top: 269px;
    list-style: none;
  }
  .contact-item {
    display: flex;
    align-items: center;
    height: 43.5px;
    font-size: 18px;
    font-weight: 400;
  }
  .contact-icon {
    width: 64px;
    flex: 0 0 64px;
    display: flex;
    justify-content: flex-end;
    padding-right: 8px;
  }
  .contact-icon svg { display: block; }
  .contact-text { padding-left: 10px; }
  .contact-text--address { letter-spacing: -0.4px; font-size: 17px; }
  .stripe-graphic {
    position: absolute;
    left: 639px;
    top: 0;
    width: 305px;
    height: 370px;
    background:
      radial-gradient(ellipse 150px 120px at 170px 140px, rgba(224,105,74,0.35) 0%, rgba(224,105,74,0) 100%),
      radial-gradient(ellipse 140px 170px at 200px 200px, rgba(138,136,136,0.25) 0%, rgba(138,136,136,0) 100%);
  }
</style>
</head>
<body>
  <section class="business-card">
    <h1 class="holder-name">GREG HALLOWAY</h1>
    <p class="licence-number">Contractor Lic No 5143K</p>

    <div class="stripe-graphic" role="img" aria-label="Crossed orange and silver brush-stroke stripes with dashed stitching lines, echoing the company shirt graphics"></div>

    <div class="contact-tab"></div>
    <ul class="contact-list">
      <li class="contact-item">
        <span class="contact-icon">
          <svg width="16" height="24" viewBox="0 0 16 24" aria-hidden="true">
            <path d="M8 0C3.6 0 0 3.5 0 7.9 0 13.6 8 24 8 24s8-10.4 8-16.1C16 3.5 12.4 0 8 0z" fill="#fff"/>
            <circle cx="8" cy="8" r="3" fill="var(--flouro-orange)"/>
          </svg>
        </span>
        <span class="contact-text contact-text--address">P.O. Box 863 TALLOWOOD NSW 2164</span>
      </li>
      <li class="contact-item">
        <span class="contact-icon">
          <svg width="20" height="16" viewBox="0 0 20 16" aria-hidden="true">
            <path d="M1 5C1 2 5 1 10 1s9 1 9 4v1.5h-4.5V4.5h-9V6.5H1z" fill="#fff"/>
            <path d="M6 7h8l4 4v4H2v-4z" fill="#fff"/>
            <circle cx="10" cy="11" r="2" fill="var(--flouro-orange)"/>
          </svg>
        </span>
        <span class="contact-text">0400 518 067</span>
      </li>
      <li class="contact-item">
        <span class="contact-icon">
          <svg width="20" height="15" viewBox="0 0 20 15" aria-hidden="true">
            <rect x="0" y="0" width="20" height="15" fill="#fff"/>
            <path d="M1 1l9 7 9-7" fill="none" stroke="var(--flouro-orange)" stroke-width="1.5"/>
          </svg>
        </span>
        <span class="contact-text">greg@velkorelectrical.com.au</span>
      </li>
      <li class="contact-item">
        <span class="contact-icon">
          <svg width="20" height="20" viewBox="0 0 20 20" aria-hidden="true">
            <g fill="none" stroke="#fff" stroke-width="2.2" stroke-linecap="round">
              <path d="M8.5 11.5a4 4 0 0 0 5.6 0l3-3a4 4 0 0 0-5.6-5.6l-1.2 1.2"/>
              <path d="M11.5 8.5a4 4 0 0 0-5.6 0l-3 3a4 4 0 0 0 5.6 5.6l1.2-1.2"/>
            </g>
          </svg>
        </span>
        <span class="contact-text">www.velkorgroup.com</span>
      </li>
    </ul>
  </section>
</body>
</html>
```